Website for Architecture & Interior Design firm

We are architecture and interior design firm looking for website design, word press based, smooth, elegant and easy to use for visitors. It should be easy to navigate using a mobile phone, with the ability to change pictures easily. It is a Bilingual website, (English: left to right, Arabic: right to left). A button in the menu bar is required to change the language, At first, we expect an English version, then we will help the designer by providing Arabic translation for any part of the website. Our website main purpose is to display our works in a picture format (Portfolio) to our clients, which mainly consist of four galleries from our (Services) as follow: 1- Architecture 2- Interior Design 3- Project Management 4- Importing from Abroad - Each service will have its page, which displays projects(items) in thumbnail format with simple text, which deploys (when clicked) into Fullscreen gallery to show the items related pictures (Dark gray or black background). - Navigation buttons/arrows are required, (X) button to close the navigation. - This is a very important part, the user experience in PC/Browser mode or Mobile mode should be easy, error-free and fast. Our homepage consists of four main elements: A- Edge to edge picture (Changing in a smooth transitional way, Random pictures from our Services) with our Logo, also persistent menu bar in the top (Home | About Us | Architecture | Interior design | Project Management | Importing from Abroad) + Social media icons B- Photo tiles (Random pictures from our Services) C- Our Services in a fixed 4-tile picture (Clickable) D- Contact Section (Simple name, contact number, message form) We expect the final service should be: 1- a fully functioning website, WordPress based, ready to be used by visitors 2- full content filling, we will contact the designer and provide the material (texture, text,etc..)
Colors
Designer to choose colors to be used in the design.
Look and feel
Each slider illustrates characteristics of the customer's brand and the style your logo design should communicate.

```html
<!DOCTYPE html>
<html lang="en">
<head>
<meta charset="utf-8">
<title>Meridian Architecture &amp; Interior Design</title>
<link rel="stylesheet" href="https://fonts.googleapis.com/css2?family=Montserrat:wght@400;500;600;700&family=Roboto:wght@300;400;500&display=swap">
<style>
  :root {
    --blue: #3d9bff;
    --ink: #1c1d20;
    --dark: #1f2024;
    --grey-text: #8a8d93;
    --line: #cfd3d8;
    --white: #ffffff;
    --label-bar: rgba(40, 40, 44, 0.72);
  }
  * { box-sizing: border-box; margin: 0; padding: 0; }
  html, body { width: 1200px; height: 1200px; overflow: hidden; background: var(--white); }
  body { font-family: "Roboto", Arial, sans-serif; color: var(--ink); }

  .site {
    position: absolute; left: 363px; top: 40px;
    width: 592px; height: 1400px;
    transform: scale(0.8); transform-origin: 0 0;
    background: var(--white);
    box-shadow: 0 0 14px rgba(0,0,0,0.08);
    overflow: hidden;
  }
  .abs { position: absolute; }

  /* header */
  .topbar { left: 0; top: 0; width: 592px; height: 30px; background: var(--white); border-bottom: 1px solid #eceef0; }
  .brand { left: 12px; top: 9px; display: flex; align-items: center; gap: 5px; }
  .brand-mark { width: 11px; height: 11px; background: var(--blue); }
  .brand-name { font-family: "Montserrat", sans-serif; font-size: 7px; font-weight: 600; letter-spacing: 1.5px; color: #4a5058; }
  .social { right: 64px; top: 12px; display: flex; gap: 8px; align-items: center; }
  .social span { width: 5px; height: 5px; border-radius: 50%; background: #6b7078; display: block; }
  .lang { right: 66px; top: 11px; font-family: "Montserrat", sans-serif; font-size: 5px; color: var(--blue); letter-spacing: 0.5px; }
  .social { right: 88px; }
  .menu-icon { right: 14px; top: 11px; }

  /* hero */
  .hero { left: 0; top: 30px; width: 592px; height: 302px; overflow: hidden;
    background: linear-gradient(100deg, #3b3a38 0%, #55524d 35%, #6d6862 60%, #4a4743 100%); }
  .hero-shade { inset: 0; background: linear-gradient(90deg, rgba(20,20,20,0.45) 0%, rgba(20,20,20,0.15) 60%, rgba(20,20,20,0.3) 100%); }
  .eyebrow { left: 14px; top: 72px; display: flex; align-items: center; gap: 5px;
    font-family: "Montserrat", sans-serif; font-size: 7px; letter-spacing: 1.5px; color: #e6e6e6; }
  .eyebrow::before { content: ""; width: 33px; height: 1px; background: #d0d0d0; }
  .welcome { left: 52px; top: 94px; font-family: "Montserrat", sans-serif; font-size: 7.5px; letter-spacing: 1.2px; line-height: 12px; color: #e8e8e8; }
  .headline { left: 52px; top: 130px; font-family: "Montserrat", sans-serif; font-weight: 700; font-size: 16px; letter-spacing: 3.6px; line-height: 22px; color: var(--white); }
  .btn-outline { left: 52px; top: 182px; width: 75px; height: 19px; border: 1px solid var(--blue);
    font-family: "Montserrat", sans-serif; font-size: 5.5px; letter-spacing: 1.2px; color: #e6e6e6;
    display: flex; align-items: center; justify-content: center; }
  .hero-frame { left: 422px; top: 72px; width: 75px; height: 127px; border: 2px solid var(--blue); }
  .hero-thumb { left: 443px; top: 91px; width: 89px; height: 89px;
    background: linear-gradient(160deg, #f2f2f0 0%, #d9dadb 55%, #9ea4ab 100%); box-shadow: 0 2px 8px rgba(0,0,0,0.35); }
  .slide-dots { left: 549px; top: 122px; display: flex; flex-direction: column; gap: 5px; }
  .slide-dots span { width: 3px; height: 3px; background: var(--white); display: block; }
  .slide-count { left: 518px; top: 255px; font-family: "Montserrat", sans-serif; font-size: 6px; color: #f0f0f0; }
  .slide-next { left: 547px; top: 253px; }
  .scroll-cue { left: 290px; top: 278px; }

  /* tiles */
  .tile { overflow: hidden; }
  .tile-blue { left: 0; top: 332px; width: 148px; height: 195px; background: var(--blue);
    display: flex; align-items: center; justify-content: center; text-align: center;
    font-family: "Montserrat", sans-serif; font-weight: 700; font-size: 15px; letter-spacing: 3.5px; line-height: 22px; color: var(--white); padding-top: 24px; }
  .tile-black { left: 296px; top: 527px; width: 148px; height: 130px; background: var(--dark);
    display: flex; align-items: center; justify-content: center;
    font-family: "Montserrat", sans-serif; font-weight: 700; font-size: 15px; letter-spacing: 3.5px; color: var(--white); padding-top: 14px; }
  .intro-panel { left: 296px; top: 332px; width: 296px; height: 195px;
    background: linear-gradient(120deg, #ffffff 0%, #f7f8f9 55%, #ece6dc 80%, #d9b48a 100%); }
  .intro-title { left: 22px; top: 24px; font-family: "Roboto", sans-serif; font-weight: 300; font-size: 18px; line-height: 26px; color: #2b2d31; }
  .intro-title em { font-style: normal; color: var(--blue); }
  .intro-body { left: 22px; top: 82px; width: 156px; font-size: 5.3px; line-height: 9px; color: var(--grey-text); }

  /* services */
  .section-title { left: 0; width: 592px; text-align: center; font-family: "Roboto", sans-serif; font-weight: 300; font-size: 19px; color: #2b2d31; }
  .section-title em { font-style: normal; color: var(--blue); }
  .section-lede { left: 146px; width: 300px; text-align: center; font-size: 5.3px; line-height: 9.5px; color: var(--grey-text); }
  .service { top: 952px; width: 148px; height: 195px; overflow: hidden; }
  .service-label { left: 0; bottom: 0; width: 148px; height: 42px; background: var(--label-bar);
    display: flex; flex-direction: column; align-items: center; justify-content: center; gap: 6px;
    font-family: "Roboto", sans-serif; font-weight: 500; font-size: 7.5px; color: var(--white); }
  .service-label::after { content: ""; width: 78px; height: 1px; background: rgba(255,255,255,0.6); }
  .feature-frame { left: 8px; top: 10px; width: 132px; height: 175px; border: 1px solid #8a7a4e; }
  .feature-box { left: 16px; top: 40px; width: 116px; height: 100px; background: #17181b; border: 1px solid #3a3a3a;
    text-align: center; padding: 12px 8px 0; }
  .feature-box h3 { font-family: "Roboto", sans-serif; font-weight: 500; font-size: 9px; color: var(--blue); margin-bottom: 10px; }
  .feature-box p { font-size: 5.2px; line-height: 9px; color: #d6d6d6; }
  .feature-btn { left: 36px; top: 70px; width: 62px; height: 17px; border: 1px solid var(--blue);
    font-family: "Montserrat", sans-serif; font-size: 5.2px; letter-spacing: 1.2px; color: #e6e6e6;
    display: flex; align-items: center; justify-content: center; }

  /* contact */
  .contact { left: 0; top: 1147px; width: 592px; height: 220px;
    background-color: #fbfbfc; background-image: radial-gradient(#e7e9ec 0.7px, transparent 0.8px); background-size: 8px 8px; }
  .field { background: var(--white); border: 1px solid #9fa4aa; font-size: 5.5px; color: #8a8d93; padding: 6px 8px; }
  .submit { left: 79px; top: 168px; width: 104px; height: 17px; background: var(--blue);
    font-family: "Montserrat", sans-serif; font-size: 5px; letter-spacing: 1.3px; color: var(--white);
    display: flex; align-items: center; justify-content: center; }

  .footer { left: 0; top: 1367px; width: 592px; height: 33px; background: var(--ink);
    display: flex; align-items: center; justify-content: center; font-size: 5.8px; color: #e6e6e6; }
  .footer em { font-style: normal; color: var(--blue); }
</style>
</head>
<body>
<div class="site">

  <header class="abs topbar">
    <div class="abs brand"><span class="brand-mark"></span><span class="brand-name">MERIDIAN</span></div>
    <div class="abs social" aria-label="Social links"><span></span><span></span><span></span><span></span></div>
    <div class="abs lang">EN</div>
    <svg class="abs menu-icon" width="11" height="8" viewBox="0 0 11 8"><path d="M0 1h11M2 4h9M0 7h11" stroke="#33363b" stroke-width="1"/></svg>
  </header>

  <section class="abs hero" role="img" aria-label="Architect working at a desk beside a white scale model of a house, colour swatches and drawings">
    <div class="abs hero-shade"></div>
    <div class="abs eyebrow">INTRODUCE</div>
    <div class="abs welcome">Welcome To<br>Meridian Architecture &amp; Interior Design</div>
    <h1 class="abs headline">IMAGINING IS KEY<br>TOMORE CREATIVE</h1>
    <div class="abs btn-outline">OUR PORTFOLIO</div>
    <div class="abs hero-frame"></div>
    <div class="abs hero-thumb" role="img" aria-label="Bright white living room with a sofa and a tree mural"></div>
    <div class="abs slide-dots"><span></span><span></span><span></span><span></span></div>
    <div class="abs slide-count">01 / 05</div>
    <svg class="abs slide-next" width="6" height="10" viewBox="0 0 6 10"><path d="M1 1l4 4-4 4" fill="none" stroke="#e6e6e6" stroke-width="1"/></svg>
    <svg class="abs scroll-cue" width="12" height="7" viewBox="0 0 12 7"><path d="M1 1l5 5 5-5" fill="none" stroke="#e6e6e6" stroke-width="1"/></svg>
  </section>

  <div class="abs tile tile-blue">LOREMIP<br>SUM</div>
  <div class="abs tile" style="left:148px;top:332px;width:148px;height:195px;background:linear-gradient(140deg,#e8e8e8,#8c8c8c 50%,#3a3a3a);" role="img" aria-label="Black and white atrium with a faceted glass roof"></div>
  <div class="abs intro-panel" role="img" aria-label="Desk corner with a notebook, pencil and potted plant">
    <h2 class="abs intro-title">Lorem ipsum <em>dolor sit</em><br><em>amet dictum</em> ante tempor</h2>
    <p class="abs intro-body">Every project begins with a careful look at how people live and work. We shape calm, lasting spaces where light, material and proportion come together in balance, from first sketch to final handover.</p>
  </div>

  <div class="abs tile" style="left:0;top:527px;width:148px;height:130px;background:linear-gradient(160deg,#f4f4f4,#c9c9c9 70%,#8f8f8f);" role="img" aria-label="Line sketch of a furnished interior"></div>
  <div class="abs tile" style="left:148px;top:527px;width:148px;height:130px;background:linear-gradient(180deg,#9a8a73,#c8b79c 45%,#ece8e2 80%);" role="img" aria-label="Wood panelled bedroom with a white bed"></div>
  <div class="abs tile-black">ABOUT</div>
  <div class="abs tile" style="left:444px;top:527px;width:148px;height:130px;background:linear-gradient(170deg,#efece8,#d8d0c4 55%,#9e8f7a);" role="img" aria-label="Bright living room with a white sofa and patterned cushions"></div>

  <div class="abs tile" style="left:0;top:657px;width:148px;height:195px;background:linear-gradient(150deg,#d9dadc,#8f8a86 45%,#3b3d42);" role="img" aria-label="Hands holding a tablet over floor plans and colour swatches"></div>
  <div class="abs tile" style="left:148px;top:657px;width:296px;height:195px;background:radial-gradient(ellipse at 50% 40%,#d7b48b 0%,#b07d4c 40%,#7d4f27 100%);" role="img" aria-label="Curved timber slat ceiling"></div>
  <div class="abs tile" style="left:444px;top:657px;width:148px;height:195px;background:linear-gradient(180deg,#3a3b3e,#55565a 45%,#6e6862 75%,#8a6a45);" role="img" aria-label="Grey sofa with yellow cushions against a dark brick wall"></div>

  <h2 class="abs section-title" style="top:888px;">Our Main <em>Services</em></h2>
  <p class="abs section-lede" style="top:920px;">We design buildings and interiors that feel clear, warm and useful, and we manage every stage with care. Browse our four services below to see selected work.</p>

  <div class="abs service" style="left:0;background:linear-gradient(145deg,#d9d9d9,#b48a4c 40%,#6e5330 75%,#3a3026);" role="img" aria-label="Timber lattice roof structure">
    <div class="abs service-label">Architecture</div>
  </div>
  <div class="abs service" style="left:148px;background:linear-gradient(180deg,#2f3033,#3c3c3e 60%,#1f1f21);" role="img" aria-label="Dark upholstered interior">
    <div class="abs feature-frame"></div>
    <div class="abs feature-box">
      <h3>Interior Design</h3>
      <p>Bring any room back to life and keep it looking fresh with our range of interior work.</p>
      <div class="abs feature-btn">KNOW MORE</div>
    </div>
  </div>
  <div class="abs service" style="left:296px;background:linear-gradient(180deg,#f2f2f2,#dcdcdc 45%,#6d4a33 62%,#efefef 80%,#5a3a28);" role="img" aria-label="White kitchen with pendant lights and walnut shelving">
    <div class="abs service-label">Project Management</div>
  </div>
  <div class="abs service" style="left:444px;background:linear-gradient(90deg,#2a3344,#5f6670 25%,#a3a6aa 60%,#8e9195);" role="img" aria-label="Building facade with grey concrete panels">
    <div class="abs service-label">Importing from Abroad</div>
  </div>

  <section class="abs contact">
    <h2 class="abs section-title" style="top:36px;"><em>Contact</em> Us</h2>
    <p class="abs section-lede" style="top:68px;">Tell us about your space and your plans. Leave your name and number, and our team will call you back within two working days.</p>
    <div class="abs field" style="left:79px;top:100px;width:210px;height:23px;">Your name</div>
    <div class="abs field" style="left:79px;top:131px;width:210px;height:23px;">Contact number</div>
    <div class="abs field" style="left:302px;top:100px;width:210px;height:54px;">Message</div>
    <div class="abs submit">SUBMIT</div>
  </section>

  <footer class="abs footer">@2019&nbsp;<em>Meridian Architecture &amp; Interior Design</em>&nbsp;All Rights Reserved.</footer>

</div>
</body>
</html>
```